Real Estate "For Sale" Sign for construction company

We need a sign that we can use to hang on a post and place on the road when we sell a property. The sign will be simple and will need to mainly feature our logo (files attached), as well as the words "For Sale", and then our phone number "(555) 617 3489". The sign will hang on a post that'll look something like the attached picture.

Target Market(s)

Home buyers

Industry/Entity Type

Real Estate

Font styles to use
Serif
Sans Serif

Colors
0054AA
0677BA
7BADD7
CADEEF
E8F1F8
0094D4
00A9DD
6FCCEA
C7EBF8
E9F6FB

Requirements
Must have
• For Sale & our phone number

```html
<!DOCTYPE html>
<html lang="en">
<head>
<meta charset="UTF-8">
<title>For Sale Yard Sign</title>
<link rel="stylesheet" href="https://fonts.googleapis.com/css2?family=League+Spartan:wght@500;700&display=swap">
<style>
  :root {
    --sign-sky: #8fd8f7;
    --sign-navy: #141f4a;
    --page-bg: #ffffff;
  }
  html, body {
    margin: 0;
    padding: 0;
    width: 1200px;
    height: 800px;
    overflow: hidden;
    background: var(--page-bg);
  }
  .canvas {
    position: relative;
    width: 1200px;
    height: 800px;
  }
  .sign {
    position: absolute;
    left: 280px;
    top: 75px;
    width: 640px;
    height: 650px;
    background: var(--sign-sky);
    border-radius: 7px;
    overflow: hidden;
    font-family: "League Spartan", "Helvetica Neue", Arial, sans-serif;
    color: var(--sign-navy);
    text-align: center;
  }
  .sign__rail {
    position: absolute;
    top: 0;
    width: 28px;
    height: 100%;
    background: var(--sign-navy);
  }
  .sign__rail--left { left: 0; }
  .sign__rail--right { right: 0; }
  .sign__notch {
    position: absolute;
    top: 0;
    left: 50%;
    width: 28px;
    height: 34px;
    margin-left: -14px;
    background: var(--sign-navy);
  }
  .sign__peak {
    position: absolute;
    bottom: 0;
    left: 50%;
    width: 172px;
    height: 28px;
    margin-left: -86px;
    background: var(--sign-navy);
    clip-path: polygon(50% 0, 100% 100%, 0 100%);
  }
  .sign__headline {
    position: absolute;
    top: 118px;
    left: 0;
    width: 100%;
    margin: 0;
    font-size: 86px;
    font-weight: 700;
    letter-spacing: 1px;
    line-height: 1;
  }
  .sign__brand {
    position: absolute;
    top: 318px;
    left: 0;
    width: 100%;
    margin: 0;
    font-size: 33px;
    font-weight: 500;
    line-height: 1;
  }
  .sign__prompt {
    position: absolute;
    top: 436px;
    left: 0;
    width: 100%;
    margin: 0;
    font-size: 36px;
    font-weight: 500;
    line-height: 1;
  }
  .sign__phone {
    position: absolute;
    top: 500px;
    left: 0;
    width: 100%;
    margin: 0;
    font-size: 56px;
    font-weight: 700;
    line-height: 1;
  }
</style>
</head>
<body>
  <main class="canvas">
    <section class="sign">
      <div class="sign__rail sign__rail--left"></div>
      <div class="sign__rail sign__rail--right"></div>
      <div class="sign__notch"></div>
      <h1 class="sign__headline">FOR SALE</h1>
      <p class="sign__brand">Ridgeline Crest Properties</p>
      <p class="sign__prompt">Call Us Today At:</p>
      <p class="sign__phone">(555) 617 3489</p>
      <div class="sign__peak"></div>
    </section>
  </main>
</body>
</html>
```